Qorvel Consulting

We focus on Data Recovery but we also do Network Security. We recover data from all types of hard drive form factors 3.5", 2.5", 1", 1.8", 5.25", 8" with any kind of interface IDE(PATA), SATA, mSATA, SCSI, SAS and Fibre Channel. All RAID Arrays 0, 1, 2, 3, 4, 5, 10 including nested levels like RAID 0+1, 1+0, 100, 0+3, 50 and 60, flash drives, like tablets, cellphones, usb drives, memory cards(SD, miniSD, Data Wafer(tavik))

Actually you can gather any information or text from any data recovery site, cause is usually the same info, we would probably change a couple of things from the description so it wont look the same. One thing though, we want to make clear to users not to attempt data recovery themselves and to ship the faulty device to us, maybe we can illustrate this?

the Data Recovery link can have sub menus like "Data Recovery Process - Data Recovery Services - F.A.Q"

the Penetration Testing can have sub menus like "F.A.Q - Pentest Process - Pentest Services"

Here are links from website so you gather information:

-http://www.mydiskwentdark.example/

-http://www.bitrescuelabsrecovery.example/

-http://www.pulvenbytes.example/

http://fetchlostfiles.example/lp/hard-drive-recovery.aspx?src=Brovix&gclid=ZTRWq4XplnQMDA-kwPbcf7HE2s
http://www.qulm.example/
http://www.venbrisfield.example/data-recovery/
http://www.tzwdatarecovery.example/

thanks.

Target Market(s)

Any PC user

Industry/Entity Type

Data Recovery

Requirements
Must have
• - Language and geographic navigation
- Home page navigation
- Global navigation
- Breadcrumbs
Nice to have
• - Sliders
-Drop down navigation

```html
<!DOCTYPE html>
<html lang="en">
<head>
<meta charset="utf-8">
<title>Qorvel Consulting — Data Recovery</title>
<link href="https://fonts.googleapis.com/css2?family=Arimo:wght@400;700&family=Lustria&family=Cabin:wght@500&family=Fredoka:wght@500&display=swap" rel="stylesheet">
<style>
:root{
  --orange:#f68312;
  --orange-light:#fb9b2e;
  --orange-text:#f05a0e;
  --brown:#6a2d07;
  --page-bg:#f3f3f3;
  --white:#ffffff;
  --ink:#222222;
  --body-text:#666666;
  --soft-box:#f2f2f6;
  --nav-top:#ffffff;
  --nav-bottom:#d9d9d9;
  --footer:#4a4a4a;
  --footer-bottom:#353535;
  --navy:#1d3d63;
}
*{box-sizing:border-box;margin:0;padding:0}
html,body{width:1200px;height:1056px;overflow:hidden;background:var(--page-bg)}
body{font-family:"Arimo",Arial,sans-serif;color:var(--ink)}
.canvas{position:relative;width:1136px;height:1000px;transform:scale(1.0563);transform-origin:0 0;background:var(--page-bg)}
.abs{position:absolute}

/* header */
.site-header{left:0;top:0;width:1136px;height:94px;background:linear-gradient(#f7850f,#f98e1c 60%,#f47c05)}
.brand{left:213px;top:0;width:171px;height:85px;background:var(--white);box-shadow:4px 4px 6px rgba(0,0,0,.25);display:flex;align-items:center;justify-content:center;gap:7px}
.brand-dot{width:12px;height:12px;border-radius:50%;background:var(--orange)}
.brand-name{font-size:16px;font-weight:700;color:var(--orange);white-space:nowrap}
.call-now{right:226px;top:12px;color:var(--white);font-size:20px;letter-spacing:.5px;text-shadow:1px 1px 2px rgba(0,0,0,.3);white-space:nowrap}
.call-now .small-caps{font-variant:small-caps}
.search{left:759px;top:50px;width:141px;height:20px;background:var(--white);border-radius:4px;box-shadow:0 1px 2px rgba(0,0,0,.3);display:flex}
.search span{flex:1;font-size:8px;color:#444;padding:6px 5px}
.search .search-btn{flex:0 0 26px;border-left:1px solid #ddd;display:flex;align-items:center;justify-content:center;padding:0}

/* column */
.page-column{left:213px;top:94px;width:710px;height:748px;background:var(--white);border-left:1px solid #e4e4e4;border-right:1px solid #e4e4e4}

/* nav */
.main-nav{left:213px;top:94px;width:710px;height:40px;background:linear-gradient(var(--nav-top),var(--nav-bottom));display:flex;border-radius:0 0 4px 4px}
.main-nav a{height:40px;display:flex;align-items:center;justify-content:center;font-size:11px;color:#222;text-decoration:none;border-right:1px solid #c9c9c9;letter-spacing:.3px;white-space:nowrap}
.main-nav a:last-child{border-right:none}

/* hero */
.hero{left:213px;top:134px;width:710px;height:246px;background:linear-gradient(90deg,#f3f3f3,#fbfbfb 50%,#eeeeee)}
.hero-photo{left:620px;top:134px;width:303px;height:246px;background:linear-gradient(90deg,#f0f0f0,#e3d7d0 40%,#8a5a48 75%,#d9cfca)}
.hero-banner{left:213px;top:160px;width:422px;height:45px;background:linear-gradient(var(--orange-light),var(--orange));display:flex;align-items:center;padding-left:15px;font-family:"Lustria",Georgia,serif;color:var(--white);font-size:13.5px;white-space:nowrap;letter-spacing:-.1px}
.quote-btn{left:635px;top:158px;width:62px;height:48px;background:var(--brown);color:var(--white);padding:9px 0 0 8px;box-shadow:2px 2px 3px rgba(0,0,0,.3);white-space:nowrap}
.quote-btn small{display:block;font-size:6px;font-weight:700;margin-bottom:2px}
.quote-btn b{font-size:13px;letter-spacing:-.6px}
.checklist{left:275px;top:216px;list-style:none}
.checklist li{display:flex;align-items:center;gap:8px;font-size:11px;height:21.5px;color:#111;white-space:nowrap}
.tick{width:15px;height:14px;background:var(--orange-text);display:flex;align-items:center;justify-content:center;border-radius:2px}
.learn-more{left:287px;top:300px;width:116px;height:33px;border-radius:7px;background:linear-gradient(#fb6a1e,#e84a08);color:var(--white);font-family:"Fredoka",sans-serif;font-size:15px;display:flex;align-items:center;justify-content:center;letter-spacing:.5px;box-shadow:0 1px 3px rgba(0,0,0,.3)}
.drive-art{left:467px;top:292px;width:158px;height:76px;border-radius:8px;background:linear-gradient(#cfcfcf,#8f8f8f)}

/* features */
.features{left:213px;top:380px;width:710px;height:77px;background:linear-gradient(#ffffff,#ececec);display:flex;border-bottom:1px solid #ddd;border-radius:0 0 4px 4px}
.feature{flex:1;position:relative;border-right:1px solid #ddd;padding:11px 10px 0 56px}
.feature:last-child{border-right:none}
.feature-icon{position:absolute;left:6px;top:12px;width:42px;height:46px;border-radius:4px}
.feature h3{font-size:11px;font-weight:400;color:var(--orange-text);margin-bottom:4px;white-space:nowrap}
.feature p{font-size:8.5px;line-height:14px;color:#888;letter-spacing:.3px}
.feature .more{position:absolute;right:10px;bottom:6px;font-size:8px;color:var(--orange-text)}

/* sidebar */
.services{left:221px;top:471px;width:173px;height:240px;background:var(--soft-box);border-radius:6px;padding:10px 0 0 19px}
.services h2{font-size:12px;font-weight:400;color:var(--orange-text);margin-bottom:4px}
.services ul{list-style:none}
.services li{height:22px;display:flex;align-items:center;font-size:9px;border-bottom:1px solid #e8e8ec;margin-right:6px;gap:7px;white-space:nowrap}
.services li .mark{font-size:10px;color:#333}
.raid-ad{left:220px;top:718px;width:172px;height:109px;border:1px solid #ccc;background:var(--white);padding:11px 8px;color:var(--navy);font-weight:700}
.raid-ad h2{font-size:11.5px;line-height:12px;letter-spacing:-.5px;margin-bottom:6px;white-space:nowrap}
.raid-ad ul{list-style:none;font-size:11px;line-height:13px;letter-spacing:-.4px;white-space:nowrap}

/* main */
.welcome{left:405px;top:474px;width:510px}
.welcome h1{font-size:12.5px;font-weight:400;margin-bottom:5px}
.welcome p,.info-box p{font-size:8.5px;line-height:15.7px;color:var(--body-text);letter-spacing:.3px;text-align:justify}
.read-more{display:block;text-align:right;font-size:8.5px;color:var(--orange-text);margin-top:2px;letter-spacing:.4px}
.info-box{left:405px;width:506px;height:111px;background:var(--soft-box);border-radius:6px;padding:11px 8px 0 8px}
.info-box h2{font-size:11px;font-weight:400;color:#444;margin-bottom:5px}

/* footer */
.site-footer{left:0;top:842px;width:1136px;height:124px;background:var(--footer)}
.footer-col{top:856px;width:142px}
.footer-col h3{font-family:"Cabin",sans-serif;font-weight:500;font-size:12px;color:var(--white);padding-bottom:4px;border-bottom:1px dotted #888;letter-spacing:.2px;white-space:nowrap}
.footer-col ul{list-style:none;margin-top:6px}
.footer-col li{font-size:8.5px;color:#eee;height:17px;display:flex;align-items:center;gap:8px;padding-left:3px}
.footer-bottom{left:0;top:966px;width:1136px;height:34px;background:var(--footer-bottom);color:var(--white);font-size:8.5px;padding:0 225px 0 222px;display:flex;align-items:center;justify-content:space-between}
</style>
</head>
<body>
<div class="canvas">
  <header class="site-header abs"></header>
  <div class="brand abs"><span class="brand-dot"></span><span class="brand-name">Qorvel Consulting</span></div>
  <div class="call-now abs"><span class="small-caps">Call Now!</span> 00-417-382</div>
  <div class="search abs"><span>Seach</span><span class="search-btn">
    <svg width="14" height="14" viewBox="0 0 14 14"><circle cx="5.5" cy="5.5" r="4.2" fill="none" stroke="#555" stroke-width="1.4"/><line x1="8.6" y1="8.6" x2="13" y2="13" stroke="#555" stroke-width="2"/></svg></span></div>

  <div class="page-column abs"></div>

  <nav class="main-nav abs">
    <a style="width:128px">Hard Drive Recovery</a>
    <a style="width:138px">Data Recovery Training</a>
    <a style="width:157px">Presentations &amp; Resources</a>
    <a style="width:124px">Computer Forensics</a>
    <a style="width:37px">Blog</a>
    <a style="width:48px">Store</a>
    <a style="width:78px">About Us</a>
  </nav>

  <section class="hero abs"></section>
  <div class="hero-photo abs" role="img" aria-label="Photo of a smiling client giving a thumbs up"></div>
  <div class="hero-banner abs">We focus on Data Recovery but we also do Network Security</div>
  <div class="quote-btn abs"><small>Request Free</small><b>QUOTE ▸</b></div>
  <ul class="checklist abs">
    <li><span class="tick"><svg width="9" height="8" viewBox="0 0 9 8"><path d="M1 4l2.5 2.5L8 1" fill="none" stroke="#fff" stroke-width="1.6"/></svg></span>Recovers lost or deleted photos and other multimedia files.</li>
    <li><span class="tick"><svg width="9" height="8" viewBox="0 0 9 8"><path d="M1 4l2.5 2.5L8 1" fill="none" stroke="#fff" stroke-width="1.6"/></svg></span>Recovers lost data from any Vistra based storage media.</li>
    <li><span class="tick"><svg width="9" height="8" viewBox="0 0 9 8"><path d="M1 4l2.5 2.5L8 1" fill="none" stroke="#fff" stroke-width="1.6"/></svg></span>Recovers from Corvane as well as PowerCore based Marlo.</li>
  </ul>
  <div class="learn-more abs">Learn More..</div>
  <div class="drive-art abs" role="img" aria-label="Open hard drive with a stethoscope"></div>

  <section class="features abs">
    <div class="feature"><div class="feature-icon" role="img" aria-label="Presentation board illustration" style="background:linear-gradient(#f4f4f4,#bdbdbd)"></div>
      <h3>Presentations &amp; Resources</h3><p>Lorem Ipsum is simply dummy text of the printing and typesetting industry.</p><span class="more">Read More</span></div>
    <div class="feature"><div class="feature-icon" role="img" aria-label="Software box illustration" style="background:linear-gradient(#e6eef6,#8ea5bd)"></div>
      <h3>Prodcut Software</h3><p>Lorem Ipsum is simply dummy text of the printing and typesetting industry.</p><span class="more">Read More</span></div>
    <div class="feature"><div class="feature-icon" role="img" aria-label="Service level note illustration" style="background:linear-gradient(#fff27a,#e8c81a)"></div>
      <h3>Types of Services Level</h3><p>Lorem Ipsum is simply dummy text of the printing and typesetting industry.</p><span class="more">Read More</span></div>
  </section>

  <aside class="services abs">
    <h2>Services</h2>
    <ul>
      <li><span class="mark">»</span>Data Recovery Process</li>
      <li><span class="mark">»</span>Vaultline® Online Backup</li>
      <li><span class="mark">»</span>File Recovery Software</li>
      <li><span class="mark">»</span>E-mail Recovery Software</li>
      <li><span class="mark">»</span>Content Recovery Software</li>
      <li><span class="mark">»</span>Forensic Data Recovery</li>
      <li><span class="mark">»</span>Data Recovery Myths</li>
      <li><span class="mark">»</span>Desktop Recovery</li>
      <li><span class="mark">»</span>Slatepad Recovery</li>
    </ul>
  </aside>
  <div class="raid-ad abs">
    <h2>Recover your RAID Arrays &amp;<br>Hard Disks NOW!</h2>
    <ul><li>• No data, no fee!</li><li>• FREE diagnosis</li><li>• Transparent pricing up front</li><li>• Qualified, experienced staff</li></ul>
  </div>

  <main class="welcome abs">
    <h1>Welcome to Data Recovery Hospital</h1>
    <p>It has survived not only five centuries, but also the leap into electronic typesetting, remaining essentially unchanged. It was popularised in the 1960s with the release of Typeset sheets containing Lorem Ipsum passages, and more recently with desktop publishing software like Pagewright Layout including versions of Lorem Ipsum.<br>Contrary to popular belief, Lorem Ipsum is not simply random text. It has roots in a piece of classical Latin literature from 45 BC, making it over 2000 years old. Edwin Marlowe, a Latin professor at Harlow-Brook College in Virginia, looked up one of the more obscure Latin words, consectetur.</p>
    <span class="read-more">Read More</span>
  </main>
  <section class="info-box abs" style="top:600px">
    <h2>About QULM</h2>
    <p>It has survived not only five centuries, but also the leap into electronic typesetting, remaining essentially unchanged. It was popularised in the 1960s with the release of Typeset sheets containing Lorem Ipsum passages, and more recently was popularised in the 1960s with the release of Typeset sheets containing Lorem Ipsum passages, and more recently with desktop publishing software like Pagewright Layout including versions of Lorem Ipsum.</p>
  </section>
  <section class="info-box abs" style="top:719px">
    <h2>Why Choose QULM?</h2>
    <p>It has survived not only five centuries, but also the leap into electronic typesetting, remaining essentially unchanged. It was popularised in the 1960s with the release of Typeset sheets containing Lorem Ipsum passages, and more recently was popularised in the 1960s with the release of Typeset sheets containing Lorem Ipsum passages, and more recently with desktop publishing software like Pagewright Layout including versions of Lorem Ipsum.</p>
  </section>

  <footer class="site-footer abs"></footer>
  <div class="footer-col abs" style="left:233px"><h3>SOFTWARE &amp; TOOLS</h3><ul><li>→ Category 1</li><li>→ Category 2</li><li>→ Category 3</li><li>→ Category 4</li></ul></div>
  <div class="footer-col abs" style="left:434px;width:144px"><h3>SERVICES &amp; SOLUTIONS</h3><ul><li>→ Category 1</li><li>→ Category 2</li><li>→ Category 3</li><li>→ Category 4</li></ul></div>
  <div class="footer-col abs" style="left:631px;width:120px"><h3 style="padding-left:7px">BLOG</h3><ul><li>→ Category 1</li><li>→ Category 2</li><li>→ Category 3</li><li>→ Category 4</li></ul></div>
  <div class="footer-col abs" style="left:785px;width:122px"><h3>COMPANY</h3><ul><li>→ Category 1</li><li>→ Category 2</li><li>→ Category 3</li><li>→ Category 4</li></ul></div>
  <div class="footer-bottom abs"><span>Copyright © 2013 Qorvelconsulting.example . All Rights Reserved.</span><span>Powered by brightlane software solutions</span></div>
</div>
</body>
</html>
```